QVLT Meridian LLC Website

Basic website for a start up business in the defense and federal space. If we could have intelligence analysis and technology as a focus that would be great. Looking to use our core colors but a lighter set of web pages would be preferable

Target Market(s)

Defense

Coding

Coded - Design and coding required

Number of Pages Required

3 page

```html
<!DOCTYPE html>
<html lang="en">
<head>
<meta charset="utf-8">
<title>QVLT Meridian LLC</title>
<link rel="stylesheet" href="https://fonts.googleapis.com/css2?family=Red+Hat+Display:wght@400;500;600;700;800&family=Roboto:wght@400;500&display=swap">
<style>
:root{
  --red:#c4073a;
  --dark:#1d1a1f;
  --ink:#2a2a2e;
  --muted:#5d5b60;
  --panel:#f2f0f3;
  --field:#f1eff2;
  --white:#ffffff;
}
*{box-sizing:border-box;margin:0;padding:0}
html,body{width:1200px;height:3123px;overflow:hidden;background:var(--white)}
body{font-family:"Red Hat Display",sans-serif;color:var(--ink)}
.page{position:relative;width:1200px;height:3123px;overflow:hidden}
.abs{position:absolute}
.btn{position:absolute;display:flex;align-items:center;justify-content:center;background:var(--red);color:var(--white);border-radius:24px;font-weight:700;font-size:15px;letter-spacing:-0.2px}

/* header */
.site-header{position:absolute;left:0;top:0;width:1200px;height:90px;background:var(--white)}
.brand{position:absolute;display:flex;align-items:center;gap:10px;font-weight:800;letter-spacing:1px}
.brand-dot{width:14px;height:14px;border-radius:50%;background:var(--red)}
.header-brand{left:60px;top:28px;font-size:30px;color:var(--dark)}
.nav{position:absolute;top:37px;font-size:13px;font-weight:600;color:var(--dark)}
.nav.active{color:var(--red)}
.header-phone{left:953px;top:18px;width:186px;height:52px;border-radius:26px;font-size:16px;gap:8px}

/* hero */
.hero{position:absolute;left:0;top:90px;width:1200px;height:600px;background:linear-gradient(115deg,#0b1422 0%,#14304f 40%,#2a6aa0 65%,#1c3f66 85%,#0e2036 100%)}
.hero-title{left:60px;top:226px;font-size:60px;line-height:70px;font-weight:700;color:var(--white);letter-spacing:-0.5px}
.hero-text{left:61px;top:374px;width:450px;font-size:14px;line-height:26px;color:var(--white)}
.hero-cta{left:60px;top:479px;width:152px;height:44px;font-size:15px}
.contact-bar{position:absolute;left:190px;top:652px;width:820px;height:74px;border-radius:37px;background:var(--red);overflow:hidden}
.contact-bar-mail{position:absolute;left:465px;top:0;width:355px;height:74px;background:var(--dark);border-radius:37px 37px 37px 37px}
.bar-call{position:absolute;left:42px;top:0;height:74px;display:flex;align-items:center;gap:12px;font-family:"Roboto",sans-serif;font-size:31px;color:var(--white)}
.bar-mail{position:absolute;left:500px;top:0;height:74px;display:flex;align-items:center;gap:12px;font-family:"Roboto",sans-serif;font-size:22px;color:var(--white)}

/* welcome */
.welcome-brand{left:0;width:1200px;top:826px;justify-content:center;font-size:30px;color:var(--dark)}
.section-title{position:absolute;left:0;width:1200px;text-align:center;font-size:46px;font-weight:400;color:var(--dark);letter-spacing:-0.5px}
.section-title b,.panel-title b{color:var(--red);font-weight:800}
.center-text{position:absolute;text-align:center;font-size:14px;line-height:26px;color:var(--muted)}

/* services */
.photo{position:absolute}
.panel{position:absolute;background:var(--panel)}
.panel-title{position:absolute;font-size:39px;font-weight:400;color:var(--dark);letter-spacing:-0.5px}
.panel-text{position:absolute;width:445px;font-size:14px;line-height:26.3px;color:var(--muted)}

/* form */
.field{position:absolute;background:var(--field);border-radius:4px;font-size:12px;color:var(--muted);padding:13px 13px}

/* footer */
.footer-wave{position:absolute;left:0;top:2740px}
.foot-head{position:absolute;top:2852px;font-size:12px;font-weight:700;color:var(--white)}
.foot-link{position:absolute;font-size:12.5px;color:var(--white)}
.foot-item{position:absolute;display:flex;gap:14px;font-size:12.5px;line-height:19px;color:var(--white)}
.footer-brand{left:60px;top:2918px;font-size:34px;color:var(--white)}
.social{position:absolute;top:3002px;width:34px;height:34px;border-radius:50%}
.news-input{position:absolute;left:893px;top:2950px;width:247px;height:32px;border-radius:16px;background:#d51f4d;font-size:12px;color:var(--white);padding:9px 13px}
.news-btn{position:absolute;left:893px;top:2995px;width:247px;height:33px;border-radius:17px;background:var(--white);color:var(--dark);font-size:12px;font-weight:700;display:flex;align-items:center;justify-content:center}
.copyright{position:absolute;left:0;top:3079px;width:1200px;height:44px;background:var(--dark);color:#bdbac0;font-size:12px;display:flex;align-items:center;justify-content:center}
.copyright b{color:var(--white);margin-right:4px}
</style>
</head>
<body>
<div class="page">

  <header class="site-header">
    <div class="brand header-brand"><span class="brand-dot"></span>QVLT MERIDIAN</div>
    <span class="nav active" style="left:568px">HOME</span>
    <span class="nav" style="left:655px">ABOUT</span>
    <span class="nav" style="left:751px">SERVICES</span>
    <span class="nav" style="left:863px">CONTACT</span>
    <div class="btn header-phone">
      <svg width="18" height="18" viewBox="0 0 24 24" fill="#fff"><path d="M6.6 10.8c1.4 2.8 3.8 5.1 6.6 6.6l2.2-2.2c.3-.3.7-.4 1-.2 1.1.4 2.3.6 3.6.6.6 0 1 .4 1 1V20c0 .6-.4 1-1 1C10.6 21 3 13.4 3 4c0-.6.4-1 1-1h3.5c.6 0 1 .4 1 1 0 1.3.2 2.5.6 3.6.1.3 0 .7-.2 1z"/></svg>
      123 456 7890
    </div>
  </header>

  <section class="hero" role="img" aria-label="Analysts working at a bank of monitors in a darkened operations centre with a world map display"></section>
  <h1 class="abs hero-title">Defense and<br>Federal Space</h1>
  <p class="abs hero-text">Lorem Ipsum is simply dummy text of the printing and typesetting industry. Lorem Ipsum has been the industry's standard dummy text ever since the 1500</p>
  <div class="btn hero-cta">CONTACT US</div>

  <div class="contact-bar">
    <div class="contact-bar-mail"></div>
    <div class="bar-call">CALL US
      <svg width="44" height="44" viewBox="0 0 44 44" fill="none" stroke="#fff" stroke-width="2"><circle cx="22" cy="22" r="18"/><path d="M14 15c1-2 3-2 4 0l2 3c.6 1 0 2-1 2.5 1 3 3 5 6 6 .5-1 1.5-1.6 2.5-1l3 2c2 1 2 3 0 4-3 2-8 0-12-4s-6-9-4.5-12.5z"/></svg>
      123 456 7890</div>
    <div class="bar-mail">
      <svg width="30" height="22" viewBox="0 0 30 22" fill="none" stroke="#fff" stroke-width="2"><rect x="1" y="1" width="28" height="20" rx="2"/><path d="M1 2l14 11L29 2"/></svg>
      Info@qvltmeridianllc.com</div>
  </div>

  <div class="brand welcome-brand"><span class="brand-dot"></span>QVLT MERIDIAN</div>
  <h2 class="section-title" style="top:890px">WELCOME TO <b>QVLT MERIDIAN LLC</b></h2>
  <p class="center-text" style="left:190px;width:820px;top:961px">Lorem Ipsum is simply dummy text of the printing and typesetting industry. Lorem Ipsum has been the industry's standard dummy text ever since the 1500s, when an unknown printer took a galley of type and scrambled it to make a type specimen book. It has survived not only five centuries, but also the leap into electronic typesetting, remaining essentially unchanged.</p>
  <div class="btn" style="left:524px;top:1095px;width:152px;height:45px">READ MORE</div>

  <div class="photo" style="left:60px;top:1230px;width:540px;height:450px;background:linear-gradient(135deg,#0c2a55,#1f5fa8 45%,#0d2346)" role="img" aria-label="Two analysts reviewing a tablet in a technology operations room"></div>
  <div class="panel" style="left:600px;top:1230px;width:540px;height:450px"></div>
  <h3 class="panel-title" style="left:646px;top:1298px">DEFENSE <b>SERVICE</b></h3>
  <p class="panel-text" style="left:646px;top:1364px">Lorem Ipsum is simply dummy text of the printing and typesetting industry. Lorem Ipsum has been the industry's standard dummy text ever since the 1500s, when an unknown printer took a galley of type and scrambled it to make a type specimen book. It has survived not only five centuries, but also the leap into electronic typesetting, remaining essentially unchanged.</p>
  <div class="btn" style="left:645px;top:1551px;width:153px;height:45px">READ MORE</div>

  <div class="panel" style="left:60px;top:1680px;width:540px;height:450px"></div>
  <h3 class="panel-title" style="left:106px;top:1748px">FEDERAL <b>SPACE</b></h3>
  <p class="panel-text" style="left:106px;top:1814px">Lorem Ipsum is simply dummy text of the printing and typesetting industry. Lorem Ipsum has been the industry's standard dummy text ever since the 1500s, when an unknown printer took a galley of type and scrambled it to make a type specimen book. It has survived not only five centuries, but also the leap into electronic typesetting, remaining essentially unchanged.</p>
  <div class="btn" style="left:105px;top:2001px;width:153px;height:45px">READ MORE</div>
  <div class="photo" style="left:600px;top:1680px;width:540px;height:450px;background:radial-gradient(ellipse at 50% 45%,#3c4a5e 0%,#1c2330 55%,#0e1219 100%)" role="img" aria-label="Businessman holding a glowing display of data charts and analytics"></div>

  <h2 class="section-title" style="top:2218px">GET IN <b>TOUCH WITH US</b></h2>
  <p class="center-text" style="left:290px;width:620px;top:2287px">Lorem Ipsum is simply dummy text of the printing and typesetting industry. Lorem Ipsum has been the industry's standard dummy text ever since the 1500.</p>
  <div class="field" style="left:292px;top:2375px;width:300px;height:45px">Name</div>
  <div class="field" style="left:607px;top:2375px;width:300px;height:45px">Contact No.</div>
  <div class="field" style="left:292px;top:2435px;width:615px;height:45px">Email</div>
  <div class="field" style="left:292px;top:2495px;width:615px;height:105px">Contact No.</div>
  <div class="btn" style="left:508px;top:2615px;width:183px;height:45px">SEND MESSAGE</div>

  <svg class="footer-wave" width="1200" height="339" viewBox="0 0 1200 339"><path d="M0 157 Q 480 10 873 5 Q 1060 5 1200 70 L1200 339 L0 339 Z" fill="var(--red)"/></svg>

  <div class="brand footer-brand">QVLT MERIDIAN</div>
  <div class="social" style="left:59px;background:var(--white)"></div>
  <div class="social" style="left:104px;background:var(--dark)"></div>
  <div class="social" style="left:150px;background:var(--white)"></div>

  <div class="foot-head" style="left:339px">USEFUL LINKS</div>
  <div class="foot-link" style="left:338px;top:2896px">Home</div>
  <div class="foot-link" style="left:338px;top:2926px">About</div>
  <div class="foot-link" style="left:338px;top:2956px">Service</div>
  <div class="foot-link" style="left:338px;top:2986px">Contact</div>

  <div class="foot-head" style="left:616px">CONTACT INFO</div>
  <div class="foot-item" style="left:618px;top:2892px">
    <svg width="12" height="16" viewBox="0 0 12 16" fill="#fff"><path d="M6 0a6 6 0 0 0-6 6c0 4.5 6 10 6 10s6-5.5 6-10a6 6 0 0 0-6-6zm0 8.5A2.5 2.5 0 1 1 6 3.5a2.5 2.5 0 0 1 0 5z"/></svg>
    <span style="width:220px">Lorem Ipsum is simply dummy text and printing typesetting.</span></div>
  <div class="foot-item" style="left:616px;top:2952px;font-weight:600">
    <svg width="14" height="14" viewBox="0 0 24 24" fill="#fff"><path d="M6.6 10.8c1.4 2.8 3.8 5.1 6.6 6.6l2.2-2.2c.3-.3.7-.4 1-.2 1.1.4 2.3.6 3.6.6.6 0 1 .4 1 1V20c0 .6-.4 1-1 1C10.6 21 3 13.4 3 4c0-.6.4-1 1-1h3.5c.6 0 1 .4 1 1 0 1.3.2 2.5.6 3.6.1.3 0 .7-.2 1z"/></svg>
    123 456 7890</div>
  <div class="foot-item" style="left:616px;top:2989px">
    <svg width="15" height="12" viewBox="0 0 15 12" fill="#fff"><path d="M0 0h15v1.5L7.5 6.5 0 1.5z"/><path d="M0 3.2l7.5 5 7.5-5V12H0z"/></svg>
    info@qvltmeridian.com</div>

  <div class="foot-head" style="left:893px">NEWSLETTER</div>
  <p class="foot-link" style="left:893px;top:2892px;width:245px;line-height:19px">Subscribe to stay with us and update our latest news, service etc...</p>
  <div class="news-input">Enter email here...</div>
  <div class="news-btn">SUBSCRIBE NOW</div>

  <footer class="copyright">©&nbsp;<b>QVLT MERIDIAN</b> - 2022. All Rights Reserved.</footer>
</div>
</body>
</html>
```